Improvement of design for elearning template

Our company provides web based elearning courses for employees. We have a design layout for the different slides which can be found here: https://www.filecrate-share.com/sh/qemvirt7xnoa2lup/KLpQzRtYwMbDfHsnVcEkGaUoPi?dl=0. The content will be added later. At this point we are just looking for a design layout that works with different content types like images, text, quiz & videos. What we would ask you, is to pick randomly 1 or 2 of the elearning slides from the existing designs and suggest improvements or come up with an alternative design. The winner of the design project can work on all slides and this will be a project with a much larger budget.
Target Market(s)
Employees in large enterprises
Look and feel
Each slider illustrates characteristics of the customer's brand and the style your logo design should communicate.

```html
<!DOCTYPE html>
<html lang="en">
<head>
<meta charset="utf-8">
<title>Handling sensitive information – course start</title>
<link rel="stylesheet" href="https://fonts.googleapis.com/css2?family=Montserrat:wght@500;600;700;800&display=swap">
<style>
  :root {
    --brand-blue: #4a7bd1;
    --title-blue: #3b6fd0;
    --accent-cyan: #5fd3f3;
    --white: #ffffff;
    --side-white: #f4f5f7;
    --stage: #e9ebef;
    --photo-dark: #3a3b3d;
    --photo-mid: #58595c;
  }
  * { box-sizing: border-box; margin: 0; padding: 0; }
  html, body { width: 1200px; height: 972px; overflow: hidden; }
  body {
    background: var(--stage);
    font-family: "Montserrat", sans-serif;
    position: relative;
  }
  .slide {
    position: absolute;
    left: 0; top: 131px;
    width: 1200px; height: 710px;
    background: var(--side-white);
    overflow: hidden;
  }
  .header-band {
    position: absolute; left: 0; top: 0;
    width: 949px; height: 135px;
    background: var(--brand-blue);
  }
  .body-band {
    position: absolute; left: 0; top: 134px;
    width: 611px; height: 576px;
    background: var(--brand-blue);
  }
  .brand {
    position: absolute; left: 62px; top: 82px;
    display: flex; align-items: center; gap: 10px;
    color: var(--white);
    font-weight: 800; font-size: 28px; letter-spacing: 0.5px;
  }
  .brand-square { width: 16px; height: 16px; background: var(--white); }
  .nav {
    position: absolute; top: 52px; left: 545px;
    display: flex; gap: 34px; list-style: none;
  }
  .nav-item {
    color: var(--white); font-weight: 700; font-size: 15px; letter-spacing: 0.6px;
    display: flex; flex-direction: column; align-items: center; gap: 6px;
  }
  .nav-item svg { display: block; }
  .timer { position: absolute; left: 1062px; top: 28px; }
  .hero-photo {
    position: absolute; left: 611px; top: 135px;
    width: 511px; height: 575px;
    background: radial-gradient(ellipse at 55% 45%, var(--photo-mid) 0%, var(--photo-dark) 75%);
  }
  .title-card {
    position: absolute; left: 11px; top: 221px;
    width: 697px; height: 209px;
    background: var(--white);
    padding: 38px 0 0 50px;
  }
  .title {
    color: var(--title-blue);
    font-weight: 800; font-size: 55px; line-height: 60px; letter-spacing: 0.3px;
  }
  .features {
    position: absolute; left: 52px; top: 460px;
    display: flex; gap: 34px; list-style: none;
  }
  .feature {
    width: 80px; display: flex; flex-direction: column; align-items: center; gap: 6px;
    color: var(--white); font-size: 11px; font-weight: 500;
  }
  .start-button {
    position: absolute; left: 52px; top: 553px;
    width: 199px; height: 70px;
    border: 1.5px solid rgba(255,255,255,0.8); border-radius: 14px;
    display: flex; align-items: center; justify-content: center; gap: 10px;
    color: var(--white); font-weight: 800; font-size: 46px; letter-spacing: 0.5px;
    padding-bottom: 4px;
  }
</style>
</head>
<body>
  <main class="slide">
    <div class="header-band"></div>
    <div class="body-band"></div>

    <div class="brand"><span class="brand-square"></span>Quellwick</div>

    <ul class="nav">
      <li class="nav-item">Lessons<svg width="16" height="9"><path d="M0 0H16L8 9Z" fill="var(--accent-cyan)"/></svg></li>
      <li class="nav-item">Menu<svg width="16" height="9"><path d="M0 0H16L8 9Z" fill="var(--accent-cyan)"/></svg></li>
      <li class="nav-item">Glossary<svg width="16" height="9"><path d="M0 0H16L8 9Z" fill="var(--accent-cyan)"/></svg></li>
    </ul>

    <svg class="timer" width="86" height="86" viewBox="0 0 86 86" aria-label="30 minutes">
      <path d="M43 6 A37 37 0 1 0 78 31" fill="none" stroke="var(--title-blue)" stroke-width="3.5"/>
      <path d="M43 6 A37 37 0 0 1 66 14" fill="none" stroke="var(--title-blue)" stroke-width="3.5" stroke-dasharray="2 3"/>
      <path d="M60 2 L70 12 L58 18 Z" fill="var(--title-blue)"/>
      <text x="43" y="46" text-anchor="middle" font-family="Montserrat, sans-serif" font-weight="800" font-size="25" fill="var(--title-blue)">30</text>
      <text x="43" y="60" text-anchor="middle" font-family="Montserrat, sans-serif" font-weight="600" font-size="11" fill="var(--title-blue)">mins</text>
    </svg>

    <div class="hero-photo" role="img" aria-label="Chalk fingerprint on a blackboard with a blue magnifying glass revealing binary digits"></div>

    <section class="title-card">
      <h1 class="title">Handling sensitive<br>information</h1>
    </section>

    <ul class="features">
      <li class="feature">
        <svg width="36" height="32" viewBox="0 0 36 32"><g fill="none" stroke="var(--white)" stroke-width="2"><rect x="5" y="20" width="7" height="10"/><rect x="14" y="13" width="7" height="17"/><rect x="23" y="3" width="7" height="27"/></g></svg>
        Complexity
      </li>
      <li class="feature">
        <svg width="40" height="32" viewBox="0 0 40 32"><g fill="var(--white)"><circle cx="20" cy="8" r="5"/><path d="M11 30 Q11 15 20 15 Q29 15 29 30Z"/><circle cx="9" cy="12" r="4"/><path d="M2 30 Q2 18 9 18 Q13 18 14 21 L12 30Z"/><circle cx="31" cy="12" r="4"/><path d="M38 30 Q38 18 31 18 Q27 18 26 21 L28 30Z"/></g></svg>
        All Audience
      </li>
      <li class="feature">
        <svg width="40" height="36" viewBox="0 0 40 36"><g stroke="var(--white)" stroke-width="2" fill="var(--white)"><line x1="20" y1="22" x2="10" y2="8"/><line x1="20" y1="22" x2="22" y2="5"/><line x1="20" y1="22" x2="33" y2="10"/><line x1="20" y1="22" x2="6" y2="20"/><circle cx="10" cy="8" r="3.5"/><circle cx="22" cy="5" r="3.5"/><circle cx="33" cy="10" r="3.5"/><circle cx="6" cy="20" r="3"/><rect x="15" y="24" width="10" height="10"/></g></svg>
        Interactive
      </li>
    </ul>

    <div class="start-button">start<svg width="12" height="20"><path d="M0 0L12 10L0 20Z" fill="var(--accent-cyan)"/></svg></div>
  </main>
</body>
</html>
```